Custom Die cut yard sign

Hi!

I would love to get really eye catching creative here with some window cleaning die cut signs!

I would like the main words to stand out of just saying, "Window Cleaning"

My phone number: 612-555-0143
Website: BrindlewayMN.com

My logo but it can be small as I want the "Window Cleaning and Phone number to really pop.

It can be a creative for implying window cleaning! Die cut so maybe water? Light? Windows outlines, squeegee? I don't know it's for residential window cleaning!

Attached is my logo and the template for the die cut sign.

Thanks!

```html
<!DOCTYPE html>
<html lang="en">
<head>
<meta charset="utf-8">
<title>Brindleway Window Cleaning – Yard Sign</title>
<link href="https://fonts.googleapis.com/css2?family=Montserrat:wght@800;900&display=swap" rel="stylesheet">
<style>
  :root {
    --page-bg: #f4f4f4;
    --navy-deep: #0a1230;
    --navy-mid: #1b2a5c;
    --photo-blue: #3d4f86;
    --photo-gray: #7c86a2;
    --headline-fill: #e6f6fd;
    --headline-stroke: #2a86d6;
    --green-light: #8dcc4e;
    --green-bright: #22b33a;
    --logo-blue: #3fa6e8;
  }
  html, body {
    margin: 0;
    padding: 0;
    width: 1200px;
    height: 848px;
    overflow: hidden;
    background: var(--page-bg);
  }
  .yard-sign {
    position: absolute;
    left: 305px;
    top: 189px;
    width: 591px;
    height: 443px;
    display: block;
  }
  .sign-text {
    font-family: "Montserrat", sans-serif;
  }
  .headline {
    font-weight: 900;
    fill: var(--headline-fill);
    stroke: var(--headline-stroke);
    stroke-width: 2.2px;
    paint-order: stroke fill;
  }
  .phone {
    font-weight: 900;
    fill: url(#green-text);
  }
  .website {
    font-weight: 800;
    fill: url(#green-text);
  }
  .brand-name {
    font-weight: 900;
    fill: var(--logo-blue);
  }
</style>
</head>
<body>
<svg class="yard-sign" viewBox="0 0 591 443" xmlns="http://www.w3.org/2000/svg">
  <defs>
    <linearGradient id="photo-tone" x1="0" y1="0" x2="1" y2="0">
      <stop offset="0" stop-color="var(--navy-mid)"/>
      <stop offset="0.45" stop-color="var(--photo-blue)"/>
      <stop offset="1" stop-color="var(--photo-gray)"/>
    </linearGradient>
    <linearGradient id="bottom-fade" x1="0" y1="0" x2="0" y2="1">
      <stop offset="0" stop-color="var(--navy-deep)" stop-opacity="0"/>
      <stop offset="0.55" stop-color="var(--navy-deep)" stop-opacity="0.85"/>
      <stop offset="1" stop-color="var(--navy-deep)"/>
    </linearGradient>
    <linearGradient id="green-text" x1="0" y1="0" x2="0" y2="1">
      <stop offset="0" stop-color="var(--green-bright)"/>
      <stop offset="0.5" stop-color="var(--green-bright)"/>
      <stop offset="0.5" stop-color="var(--green-light)"/>
      <stop offset="1" stop-color="var(--green-light)"/>
    </linearGradient>
    <linearGradient id="green-band" x1="0" y1="0" x2="0" y2="1">
      <stop offset="0" stop-color="var(--green-bright)"/>
      <stop offset="1" stop-color="var(--green-light)"/>
    </linearGradient>
  </defs>

  <!-- background -->
  <rect class="sign-base" x="0" y="0" width="591" height="443" fill="var(--navy-deep)"/>
  <rect class="hero-photo" x="0" y="0" width="591" height="300" fill="url(#photo-tone)"
        role="img" aria-label="Photo of gloved hands washing a window with a soapy scrubber and squeegee"/>
  <rect class="photo-fade" x="0" y="140" width="591" height="170" fill="url(#bottom-fade)"/>

  <!-- brand -->
  <g class="brand">
    <circle cx="37" cy="52" r="9" fill="var(--logo-blue)"/>
    <text class="sign-text brand-name" x="52" y="59" font-size="19">BRINDLEWAY</text>
  </g>

  <!-- headline -->
  <text class="sign-text headline" x="61" y="196" font-size="104" textLength="457" lengthAdjust="spacingAndGlyphs">WINDOW</text>
  <text class="sign-text headline" x="35" y="284" font-size="104" textLength="533" lengthAdjust="spacingAndGlyphs">CLEANING</text>

  <!-- contact -->
  <text class="sign-text phone" x="46" y="363" font-size="84" textLength="499" lengthAdjust="spacingAndGlyphs">612 555 0143</text>
  <text class="sign-text website" x="134" y="404" font-size="38" textLength="309" lengthAdjust="spacingAndGlyphs">BrindlewayMN.COM</text>

  <!-- bottom chevron band -->
  <path class="green-band" d="M0 394 L290 437 L591 394 L591 443 L0 443 Z" fill="url(#green-band)"/>
</svg>
</body>
</html>
```